Brindle Offers is an online marketing platform.

A daily deals site for consumers a way to bring in new clients for clients and this is who the business cards are for. Industries - Food and Drink, Things To Do, Beauty and Spas, Staycations and Services.
Logo on one side.
Name - Owen Radley
Job Title - Sales Director
Phone Number - 07912358046
Email - owen@brindleoffers.co.uk
need same for second person
Name - Fiona Bracken
Job Title - Operations Director
Phone Number - 01632840275
Email - fiona@brindleoffers.co.uk
Bottom Right - Chatterbook Icon, Snapa Icon, Pipline Icon
Target Market(s)
Business owners of the above industries
Contact Information for Business Card
Name - Owen Radley
Name - Fiona Bracken
Look and feel

```html
<!DOCTYPE html>
<html lang="en">
<head>
<meta charset="utf-8">
<title>Brindle Offers – Business Cards</title>
<link href="https://fonts.googleapis.com/css2?family=Montserrat:wght@400&family=Open+Sans:wght@400;700&display=swap" rel="stylesheet">
<style>
  :root {
    --stage: #2e2e2e;
    --card: #ffffff;
    --ink: #333333;
    --blue: #0d4fa3;
    --mist: #e6e8f3;
  }
  * { margin: 0; padding: 0; box-sizing: border-box; }
  html, body { width: 1200px; height: 934px; overflow: hidden; background: var(--stage); }
  body { position: relative; font-family: "Open Sans", sans-serif; color: var(--ink); }

  .card {
    position: absolute; width: 426px; height: 263px; background: var(--card);
    box-shadow: 6px 8px 10px rgba(0,0,0,.45); overflow: hidden;
  }
  .card--front-owen { left: 143px; top: 170px; }
  .card--back-owen { left: 631px; top: 170px; }
  .card--front-fiona { left: 143px; top: 501px; }
  .card--back-fiona { left: 631px; top: 501px; }

  .brand { position: absolute; display: flex; align-items: center; }
  .brand__dot { border-radius: 50%; background: var(--blue); flex: none; }
  .brand__name { font-family: "Open Sans", sans-serif; font-weight: 700; color: var(--blue); white-space: nowrap; line-height: 1; }
  .brand__tagline { position: absolute; font-family: "Open Sans", sans-serif; color: var(--ink); white-space: nowrap; }

  .card--front .brand { left: 52px; top: 106px; }
  .card--front .brand__dot { width: 30px; height: 30px; margin-right: 7px; }
  .card--front .brand__name { font-size: 17px; }
  .card--front .brand__tagline { left: 89px; top: 140px; font-size: 9px; letter-spacing: 1px; }

  .contact { position: absolute; left: 235px; top: 79px; }
  .contact__name { font-family: "Montserrat", sans-serif; font-size: 17px; text-transform: uppercase; color: var(--ink); letter-spacing: -.2px; }
  .contact__role { font-size: 11.5px; color: var(--blue); margin-top: -2px; }
  .contact__line { display: flex; align-items: center; font-size: 10.5px; margin-top: 6px; }
  .contact__line:first-of-type { margin-top: 10px; }
  .contact__line svg { width: 9px; height: 9px; margin-right: 6px; fill: var(--blue); }
  .social { display: flex; gap: 13px; margin-top: 16px; }
  .social__mark { width: 10px; height: 10px; background: var(--blue); border-radius: 1px; }

  .halo { position: absolute; left: 125px; top: -20px; width: 176px; height: 176px; border-radius: 50%; background: var(--mist); }
  .card--back .brand { left: 95px; top: 92px; }
  .card--back .brand__dot { width: 40px; height: 40px; margin-right: 10px; }
  .card--back .brand__name { font-size: 27px; }
  .card--back .brand__tagline { left: 145px; top: 140px; font-size: 13px; letter-spacing: 1.6px; }

  .site-rule { position: absolute; left: 0; right: 0; top: 219px; height: 1px; background: var(--blue); }
  .site-url {
    position: absolute; left: 50%; top: 211px; transform: translateX(-50%); background: var(--card);
    padding: 0 6px; font-size: 10.5px; letter-spacing: 2px; color: var(--blue); white-space: nowrap;
  }
</style>
</head>
<body>

<section class="card card--front card--front-owen">
  <div class="brand"><span class="brand__dot"></span><span class="brand__name">Brindle Offers</span></div>
  <span class="brand__tagline">DINE. PLAY. UNWIND.</span>
  <div class="contact">
    <p class="contact__name">Owen Radley</p>
    <p class="contact__role">Sales Director</p>
    <p class="contact__line"><svg viewBox="0 0 10 10" aria-hidden="true"><path d="M2 0h2l1 3-1.5 1a6 6 0 0 0 2.5 2.5L7 5l3 1v2a2 2 0 0 1-2 2A8 8 0 0 1 0 2a2 2 0 0 1 2-2z"/></svg>07912358046</p>
    <p class="contact__line"><svg viewBox="0 0 10 10" aria-hidden="true"><path d="M0 2h10v6H0z M0 2l5 3 5-3" /></svg>owen@brindleoffers.co.uk</p>
    <div class="social" aria-label="Pipline, Snapa, Chatterbook">
      <span class="social__mark"></span><span class="social__mark"></span><span class="social__mark"></span>
    </div>
  </div>
</section>

<section class="card card--back card--back-owen">
  <div class="halo"></div>
  <div class="brand"><span class="brand__dot"></span><span class="brand__name">Brindle Offers</span></div>
  <span class="brand__tagline">DINE. PLAY. UNWIND.</span>
  <div class="site-rule"></div>
  <span class="site-url">www.brindleoffers.co.uk</span>
</section>

<section class="card card--front card--front-fiona">
  <div class="brand"><span class="brand__dot"></span><span class="brand__name">Brindle Offers</span></div>
  <span class="brand__tagline">DINE. PLAY. UNWIND.</span>
  <div class="contact">
    <p class="contact__name">Fiona Bracken</p>
    <p class="contact__role">Operations Director</p>
    <p class="contact__line"><svg viewBox="0 0 10 10" aria-hidden="true"><path d="M2 0h2l1 3-1.5 1a6 6 0 0 0 2.5 2.5L7 5l3 1v2a2 2 0 0 1-2 2A8 8 0 0 1 0 2a2 2 0 0 1 2-2z"/></svg>01632840275</p>
    <p class="contact__line"><svg viewBox="0 0 10 10" aria-hidden="true"><path d="M0 2h10v6H0z M0 2l5 3 5-3" /></svg>fiona@brindleoffers.co.uk</p>
    <div class="social" aria-label="Pipline, Snapa, Chatterbook">
      <span class="social__mark"></span><span class="social__mark"></span><span class="social__mark"></span>
    </div>
  </div>
</section>

<section class="card card--back card--back-fiona">
  <div class="halo"></div>
  <div class="brand"><span class="brand__dot"></span><span class="brand__name">Brindle Offers</span></div>
  <span class="brand__tagline">DINE. PLAY. UNWIND.</span>
  <div class="site-rule"></div>
  <span class="site-url">www.brindleoffers.co.uk</span>
</section>

</body>
</html>
```